Need a flyer to leave behind when visiting clients or at shows

Glossy colorful tri-fold flyer with the same information that is on my web site www.brevalinkpro.com. I am open to a little modern or creative take on the typical brochure. I created the web site so I can provide any raw files needed from it. I would also like the ability to edit this flyer in the future in Adobe Photoshop Elements

```html
<!DOCTYPE html>
<html lang="en">
<head>
<meta charset="utf-8">
<title>Brevalink Pro – Tri-fold Brochure</title>
<link rel="stylesheet" href="https://fonts.googleapis.com/css2?family=Open+Sans:wdth,wght@75..100,300..800&display=swap">
<style>
  :root {
    --navy: #2b1a5c;
    --navy-deep: #221449;
    --violet: #7a4cc6;
    --violet-soft: #9a78d6;
    --ink: #2b1a5c;
    --paper: #ffffff;
    --canvas: #f1f0f4;
    --muted: #c9bfe6;
  }
  * { box-sizing: border-box; margin: 0; padding: 0; }
  html, body { width: 1200px; height: 3000px; overflow: hidden; }
  body {
    background: var(--canvas);
    font-family: "Open Sans", Arial, sans-serif;
    color: var(--ink);
    position: relative;
  }
  .spread {
    position: absolute;
    left: 50px;
    width: 1100px;
    height: 780px;
    display: flex;
    box-shadow: 0 2px 10px rgba(40, 20, 80, .18);
    background: var(--paper);
  }
  .spread--outside { top: 180px; }
  .spread--inside { top: 1080px; }
  .panel { position: relative; width: 366.67px; height: 100%; overflow: hidden; }

  /* Outside – objectives */
  .objectives__head {
    background: var(--violet);
    color: #fff;
    height: 185px;
    padding: 52px 30px 0;
    font-weight: 800;
    font-size: 25px;
    line-height: 1.45;
    font-stretch: 85%;
    letter-spacing: .5px;
  }
  .objectives__photo {
    position: absolute; left: 0; right: 0; top: 185px; bottom: 0;
    background: linear-gradient(120deg, #f4f2f1 0%, #ece4de 35%, #e2d7cf 60%, #f1eeee 100%);
  }
  .objectives__list {
    position: absolute; top: 232px; left: 40px; width: 250px;
    list-style: none;
    font-size: 21px; line-height: 1.5; color: #2a2440;
  }
  .objectives__list li { position: relative; padding-left: 22px; margin-bottom: 22px; }
  .objectives__list li::before {
    content: ""; position: absolute; left: 0; top: 12px;
    width: 8px; height: 8px; background: #2a2440;
  }

  /* Outside – contact */
  .contact { background: var(--navy); color: #fff; }
  .contact__frame {
    position: absolute; left: 28px; right: 28px; top: 58px; bottom: 30px;
    border: 3px solid #fff;
  }
  .contact__intro {
    position: absolute; top: 92px; left: 56px; right: 56px;
    text-align: center; font-size: 15px; line-height: 2; color: #ddd6f0; font-weight: 300;
  }
  .contact__title {
    position: absolute; top: 525px; left: 0; right: 0;
    text-align: center; font-weight: 700; font-size: 21px; letter-spacing: .5px;
  }
  .contact__list { position: absolute; top: 585px; left: 60px; right: 30px; list-style: none; }
  .contact__list li {
    display: flex; align-items: center; gap: 12px;
    font-size: 17px; margin-bottom: 19px;
  }
  .contact__list li.contact__phone { font-size: 22px; font-weight: 700; }
  .contact__list li.contact__web { font-weight: 600; }
  .contact__list svg { width: 20px; height: 20px; flex: none; }

  /* Outside – cover */
  .cover {
    background: linear-gradient(160deg, #3a2a6c 0%, #4a3a78 40%, #3b2b6a 70%, #2b1b5a 100%);
    color: #fff;
  }
  .cover__photo {
    position: absolute; inset: 0 0 130px 0;
    background: radial-gradient(ellipse at 70% 65%, rgba(160,140,190,.45), rgba(60,40,110,0) 60%),
                linear-gradient(180deg, rgba(120,100,170,.25), rgba(40,25,90,.1));
  }
  .cover__tagline {
    position: absolute; top: 150px; left: 20px; right: 20px;
    text-align: center; font-size: 14px; color: #cfc6ea; font-weight: 300; line-height: 1.5;
  }
  .cover__headline {
    position: absolute; top: 232px; left: 20px; right: 20px;
    text-align: center; font-weight: 800; font-stretch: 78%;
    font-size: 33px; line-height: 1.42; letter-spacing: .3px;
  }
  .cover__band {
    position: absolute; left: 0; right: 0; bottom: 0; height: 128px;
    background: var(--violet);
    display: flex; align-items: center; justify-content: space-between; padding: 0 26px;
  }
  .brand {
    display: inline-flex; align-items: center; gap: 10px;
    color: #fff; font-weight: 700; font-size: 26px; letter-spacing: .3px;
  }
  .brand__mark { width: 14px; height: 14px; background: #fff; }
  .badge { width: 58px; height: 58px; border-radius: 50%; background: #d9d3ea; }

  /* Inside – core values */
  .values__art {
    position: absolute; left: 0; right: 0; top: 0; height: 345px;
    background: linear-gradient(135deg, #eceaf2 0%, #d9d0ee 45%, #b6a2de 70%, #efedf4 100%);
  }
  .values__title {
    position: absolute; top: 364px; left: 40px; right: 40px; height: 74px;
    background: var(--navy); color: #fff;
    display: flex; align-items: center; justify-content: center;
    font-size: 34px; font-weight: 600; letter-spacing: .5px;
  }
  .values__list {
    position: absolute; top: 475px; left: 0; right: 0; list-style: none;
    text-align: center; font-weight: 700; font-size: 17px; letter-spacing: .3px; line-height: 1.3;
  }
  .values__list li { margin-bottom: 34px; }

  /* Inside – about */
  .about { background: var(--navy); color: #fff; text-align: center; }
  .about__brand {
    margin: 36px auto 0; display: flex; justify-content: center;
  }
  .about__brand .brand { font-size: 24px; }
  .about__title { margin-top: 102px; font-size: 36px; font-weight: 600; letter-spacing: .5px; }
  .about__sub { margin-top: 28px; font-size: 26px; font-weight: 500; }
  .about__sub + p { margin: 12px 28px 0; font-size: 16px; line-height: 1.5; color: #e4def4; }

  /* Inside – services */
  .services__head {
    height: 185px; background: var(--violet); color: #fff;
    padding: 62px 0 0 120px; font-size: 40px; font-weight: 600; line-height: 1.15; text-align: center;
  }
  .services__intro {
    margin: 20px 40px 0 42px; font-size: 16px; line-height: 1.55; color: #24203a;
  }
  .services__image {
    margin: 28px auto 0; width: 244px; height: 145px;
    border: 2px solid #d8d4e0;
    background: linear-gradient(120deg, #22306a, #3c5aa8 55%, #7fa6e0);
  }
  .services__subhead { margin: 24px 0 0 42px; font-weight: 700; font-size: 15px; color: var(--navy); }
  .services__list { margin: 6px 20px 0 58px; list-style: disc; font-size: 14px; line-height: 1.65; color: #24203a; }
</style>
</head>
<body>

<section class="spread spread--outside">
  <div class="panel objectives">
    <h2 class="objectives__head">OUR<br>PRIMARY<br>OBJECTIVES</h2>
    <div class="objectives__photo" role="img" aria-label="Photo of two healthcare professionals reviewing notes at a desk"></div>
    <ul class="objectives__list">
      <li>Understand and exceed client expectations</li>
      <li>Committed to be a partner, not vendor</li>
      <li>Provide simplified change management expertise</li>
    </ul>
  </div>

  <div class="panel contact">
    <div class="contact__frame"></div>
    <p class="contact__intro">Brevalink Pro strives to assist your organization by bringing solutions that are easy to understand and allow the client to track success</p>
    <h3 class="contact__title">CONTACT US</h3>
    <ul class="contact__list">
      <li>
        <svg viewBox="0 0 20 20" aria-hidden="true"><rect x="1" y="4" width="18" height="12" rx="1.5" fill="#fff"/><path d="M1.5 5 L10 11 L18.5 5" stroke="#2b1a5c" stroke-width="1.6" fill="none"/></svg>
        dwhitfield@brevalinkpro.com
      </li>
      <li class="contact__phone">
        <svg viewBox="0 0 20 20" aria-hidden="true"><path d="M5 2 L8 2 L9 6 L7 7.5 C8 10 10 12 12.5 13 L14 11 L18 12 L18 15 C18 16.5 17 17.5 15.5 17.5 C8.5 17 3 11.5 2.5 4.5 C2.5 3 3.5 2 5 2 Z" fill="#fff"/></svg>
        555-014-2290
      </li>
      <li class="contact__web">
        <svg viewBox="0 0 20 20" aria-hidden="true"><circle cx="10" cy="10" r="8.5" fill="none" stroke="#fff" stroke-width="1.5"/><ellipse cx="10" cy="10" rx="3.5" ry="8.5" fill="none" stroke="#fff" stroke-width="1.3"/><path d="M1.5 10 H18.5" stroke="#fff" stroke-width="1.3"/></svg>
        www.brevalinkpro.com/
      </li>
    </ul>
  </div>

  <div class="panel cover">
    <div class="cover__photo" role="img" aria-label="Photo of a clinician holding a tablet, tinted purple"></div>
    <p class="cover__tagline">Providing Information Technology expertise to post-acute care providers</p>
    <h1 class="cover__headline">INCREASING THE VALUE<br>AND SECURITY OF<br>YOUR TECHNOLOGY<br>RESOURCES</h1>
    <div class="cover__band">
      <span class="brand"><span class="brand__mark"></span>Brevalink Pro</span>
      <span class="badge" role="img" aria-label="Partner badge"></span>
    </div>
  </div>
</section>

<section class="spread spread--inside">
  <div class="panel values">
    <div class="values__art" role="img" aria-label="Illustration of medical icons in hexagons beside a stethoscope"></div>
    <h2 class="values__title">CORE VALUES</h2>
    <ul class="values__list">
      <li>CLIENT FOCUSED</li>
      <li>ACCOUNTABILITY</li>
      <li>INTEGRITY</li>
      <li>PROFESSIONAL<br>DEVELOPMENT</li>
    </ul>
  </div>

  <div class="panel about">
    <div class="about__brand"><span class="brand"><span class="brand__mark"></span>Brevalink Pro</span></div>
    <h2 class="about__title">ABOUT US</h2>
    <h3 class="about__sub">Our Mission</h3>
    <p>Partner with clients to increase the value and security of their technology tools.</p>
    <h3 class="about__sub">Our Goal</h3>
    <p>Become the premiere consulting company for Information Technology in the post-acute care industries.</p>
    <h3 class="about__sub">Our Leaders</h3>
    <p>Dana Whitfield, MHA, MBA, CHCIO</p>
  </div>

  <div class="panel services">
    <h2 class="services__head">OUR<br>SERVICES</h2>
    <p class="services__intro">We understand different organizations have different needs. Brevalink Pro strives to assist your organization by bringing solutions that are easy to understand and allow the client to track success. We provide solutions based on the client's needs and desires.</p>
    <div class="services__image" role="img" aria-label="Photo of a hand touching a glowing IT network diagram"></div>
    <h3 class="services__subhead">Information Technology</h3>
    <ul class="services__list">
      <li>CIO or IT Director Services</li>
      <li>CISO or Information Security Officer</li>
      <li>Comprehensive ePHI Risk Assessments</li>
      <li>IT Department Evaluation</li>
      <li>Policy Management and Consulting</li>
      <li>On-going IT department support</li>
    </ul>
  </div>
</section>

</body>
</html>
```